Harborlane Consultants LLC web site

Harborlane Consultants LLC is a consulting and recruiting firm that provides education, perspective, guidance, and assistance to financial advisors. Dennis Malbrook is the founder of this new firm and is the only employee at this time.
Please see the attached overview which will provide much narrative describing the firm, its purpose, scope of services offered, and other useful information to help you design a web site.

Target Market(s)

US based financial advisors who are looking to transition their business to an independent ( non-employee ) business model.

Industry/Entity Type

Consultant

Coding

Coded - Design and coding required

Number of Pages Required

5+ page

Font styles to use
Sans Serif

Requirements
Must have
• all relevant pages for a basic web site : Home, About, Services offered, Contact, Resources , etc.
Nice to have
• color scheme : see logo in the attached briefing document

```html
<!DOCTYPE html>
<html lang="en">
<head>
<meta charset="utf-8">
<title>Harborlane Consultants LLC</title>
<link href="https://fonts.googleapis.com/css2?family=Cinzel:wght@400;600&family=Open+Sans:wght@400;600;700&family=Raleway:wght@500;600;700&display=swap" rel="stylesheet">
<style>
:root{
  --navy:#1d4a74;
  --blue:#2b6a9c;
  --ink:#333;
  --muted:#777;
  --grey-dark:#575757;
  --grey-hero:#8d8d8d;
  --light:#f3f4f6;
  --white:#fff;
}
*{margin:0;padding:0;box-sizing:border-box}
html,body{width:1200px;height:3988px;overflow:hidden}
body{font-family:"Open Sans",sans-serif;color:var(--ink);background:var(--white);position:relative}
.abs{position:absolute}
.btn{display:inline-block;background:var(--navy);color:var(--white);font:600 12px "Open Sans",sans-serif;padding:11px 26px;border-radius:20px;text-decoration:none}
.photo{background:linear-gradient(135deg,#c9d3dc,#8ea3b6)}

/* header */
.site-header{left:0;top:0;width:1200px;height:80px;z-index:3;display:flex;align-items:center;padding:0 60px}
.brand{display:flex;align-items:center;gap:10px;font:700 17px "Raleway",sans-serif;color:var(--navy);text-transform:uppercase;letter-spacing:1px}
.brand .dot{width:30px;height:30px;border-radius:50%;background:var(--navy)}
.nav{margin-left:auto;display:flex;align-items:center;gap:34px;font:600 13px "Open Sans",sans-serif}
.nav a{color:var(--ink);text-decoration:none}
.nav .active{color:var(--navy);border-bottom:2px solid var(--navy);padding-bottom:3px}
.nav .call{color:var(--navy)}
.nav .btn{background:var(--grey-dark);padding:9px 20px}

/* hero */
.hero{left:0;top:0;width:1200px;height:720px;background:linear-gradient(90deg,#7c7c7c,#a3a3a3 55%,#bdbdbd)}
.hero-photo{right:0;top:80px;width:560px;height:620px;background:linear-gradient(160deg,#d7dde3,#5e6f80)}
.hero-copy{left:100px;top:370px;color:var(--white)}
.hero-copy h1{font:400 40px "Cinzel",serif;letter-spacing:1px;margin-bottom:26px}
.hero-copy p{font:400 22px "Open Sans",sans-serif;line-height:1.35;width:430px;margin-bottom:34px}
.hero-wave{left:0;top:620px;width:1200px;height:160px}
.wave-mark{left:575px;width:50px;height:50px;border-radius:50%;background:var(--navy);border:6px solid var(--white)}

/* services */
.section-title{width:1200px;text-align:center;font:500 30px "Raleway",sans-serif;color:var(--grey-dark)}
.section-sub{width:1200px;text-align:center;font:400 13px "Open Sans",sans-serif;color:var(--muted)}
.circle{width:400px;height:400px;border-radius:50%;border:8px solid #e6e6e6;box-shadow:0 0 0 2px #cfcfcf}
.service{width:440px}
.service h3{font:600 18px "Raleway",sans-serif;color:var(--navy);margin-bottom:20px}
.service p{font:400 13px/1.75 "Open Sans",sans-serif;color:var(--muted);margin-bottom:24px}

/* why */
.why{left:0;top:2090px;width:1200px;height:540px}
.why-title{top:2200px;color:var(--white);font-weight:600}
.why-sub{top:2244px;color:#e6e6e6}
.stats{left:0;top:2330px;width:1200px;display:flex;justify-content:center;gap:0}
.stat{width:300px;text-align:center;color:var(--white);border-right:1px solid rgba(255,255,255,.4)}
.stat:last-child{border-right:0}
.stat .num{font:600 48px "Open Sans",sans-serif;line-height:60px;height:60px;display:flex;align-items:center;justify-content:center}
.stat .sq{width:44px;height:44px;background:var(--white);border-radius:4px}
.stat .cap{font:400 13px/1.4 "Open Sans",sans-serif;margin-top:8px}

/* resources */
.res-label{font:700 12px "Open Sans",sans-serif;color:var(--navy);margin:16px 0 10px}
.res-title{font:600 20px/1.3 "Raleway",sans-serif;color:var(--ink);margin-bottom:14px}
.res-text{font:400 12px/1.7 "Open Sans",sans-serif;color:var(--muted);margin-bottom:22px}
.card{background:var(--white);box-shadow:0 2px 10px rgba(0,0,0,.08);padding:0 0 20px}
.card .inner{padding:0 18px}

/* footer */
.footer{left:0;top:3440px;width:1200px;height:548px;background:var(--light)}
.foot-brand{left:140px;top:3640px}
.foot-contact{left:450px;top:3600px;font:400 13px/1.9 "Open Sans",sans-serif;color:var(--ink)}
.foot-contact h4,.foot-links h4{font:700 15px "Raleway",sans-serif;color:var(--navy);margin-bottom:10px}
.foot-contact b{color:var(--navy)}
.foot-links{left:760px;top:3600px;font:400 13px/1.8 "Open Sans",sans-serif}
.foot-links div{color:var(--ink)}
.map{left:900px;top:3610px;width:220px;height:200px;background:linear-gradient(135deg,#e3e9ee,#c3d3df)}
.copy{left:40px;top:3950px;font:400 11px "Open Sans",sans-serif;color:var(--muted)}
</style>
</head>
<body>

<section class="hero abs"></section>
<div class="hero-photo abs" role="img" aria-label="Portrait photograph of the founder in a suit"></div>

<header class="site-header abs">
  <div class="brand"><span class="dot"></span>Harborlane Consultants LLC</div>
  <nav class="nav">
    <a class="active" href="#">Home</a>
    <a href="#">About</a>
    <a href="#">Services</a>
    <a href="#">Resources</a>
    <a class="call" href="#">Call Us: 555-201-4830</a>
    <a class="btn" href="#">Contact Us</a>
  </nav>
</header>

<div class="hero-copy abs">
  <h1>Harborlane Consultants LLC</h1>
  <p>"Helping financial advisors to navigate their journey to independence"</p>
  <a class="btn" href="#">About Us</a>
</div>

<svg class="hero-wave abs" viewBox="0 0 1200 160" preserveAspectRatio="none" aria-hidden="true">
  <path d="M0 40 C300 120 500 60 600 70 C750 80 900 0 1200 30 L1200 160 L0 160Z" fill="var(--navy)"/>
  <path d="M0 70 C300 140 480 90 600 95 C760 100 900 30 1200 60 L1200 160 L0 160Z" fill="var(--white)"/>
</svg>
<div class="wave-mark abs" style="top:695px"></div>

<h2 class="section-title abs" style="top:752px">Client Services</h2>
<p class="section-sub abs" style="top:792px">How we work together , What to Expect</p>

<div class="circle photo abs" style="left:120px;top:840px" role="img" aria-label="Photo of hands reviewing financial charts"></div>
<div class="service abs" style="left:620px;top:900px">
  <h3>A Fiduciary Relationship for Your Business</h3>
  <p>One very important thing to know about me and how I work with clients is that I will always put your interests first. That may sound familiar to you, especially if that is how you work with your own clients, and that is exactly the approach I bring to every advisor who is exploring the path toward independence and a business of their own...</p>
  <a class="btn" href="#">Explore More</a>
</div>

<div class="service abs" style="left:90px;top:1330px">
  <h3>Services for Teams and Advisors in Transition</h3>
  <p>Making any business transition is a complex undertaking. Harborlane Consultants offers a multi-step, comprehensive process that addresses the following critical topics. I want one day for you to look back at a "seamless" journey to independence...</p>
  <a class="btn" href="#">Discover More</a>
</div>
<div class="circle photo abs" style="left:680px;top:1260px" role="img" aria-label="Photo of a team meeting around a table"></div>

<div class="circle photo abs" style="left:120px;top:1680px" role="img" aria-label="Photo of a pen over printed reports"></div>
<div class="service abs" style="left:620px;top:1790px">
  <h3>Services for Existing RIAs</h3>
  <p>Let's face it. You have a business to run. You have clients, and you have assets, both of which give you plenty to worry about. You have organic growth goals and are busy trying to achieve them. I can help you add proven experience and expertise to reach them...</p>
  <a class="btn" href="#">Explore More</a>
</div>

<svg class="why abs" viewBox="0 0 1200 540" preserveAspectRatio="none" aria-hidden="true">
  <path d="M0 60 C300 0 450 30 600 40 C800 55 950 0 1200 20 L1200 480 C900 540 700 470 600 480 C400 500 250 450 0 500Z" fill="var(--grey-dark)"/>
  <path d="M0 480 C250 430 400 480 600 460 C750 445 900 520 1200 460 L1200 540 L0 540Z" fill="var(--navy)"/>
  <path d="M0 505 C250 460 400 505 600 485 C760 470 900 540 1200 485 L1200 540 L0 540Z" fill="var(--white)"/>
</svg>
<h2 class="section-title why-title abs">Why Work With Me ?</h2>
<p class="section-sub why-sub abs">In short, experience. I have spent my entire 35 year career in this industry,<br>with the last 22 years spent in this exact endeavor...</p>
<div class="stats abs">
  <div class="stat"><div class="num">35</div><div class="cap">Years Career in This<br>Industry</div></div>
  <div class="stat"><div class="num">22</div><div class="cap">Years in this Exact<br>Endeavor</div></div>
  <div class="stat"><div class="num"><span class="sq"></span></div><div class="cap">Network Additional<br>Work History</div></div>
</div>
<a class="btn abs" style="left:490px;top:2496px" href="#">Schedule an Exploratory Meeting Now</a>

<h2 class="section-title abs" style="top:2720px">Harborlane Resources</h2>

<article class="card abs" style="left:300px;top:2790px;width:300px">
  <div class="photo" style="height:240px" role="img" aria-label="Photo of a tablet showing latest articles"></div>
  <div class="inner">
    <div class="res-label">Articles</div>
    <div class="res-title">It is a long established fact that a reader will be distracted</div>
    <p class="res-text">Lorem ipsum is simply dummy text of the printing and typesetting industry. It is a long established fact that a reader will be distracted by the readable content of a page when looking at its layout and design.</p>
    <a class="btn" href="#">Explore More</a>
  </div>
</article>

<div class="photo abs" style="left:620px;top:2790px;width:492px;height:200px" role="img" aria-label="Video thumbnail of an advisor meeting"></div>

<article class="card abs" style="left:620px;top:3010px;width:236px">
  <div class="photo" style="height:130px" role="img" aria-label="Photo of white paper documents"></div>
  <div class="inner">
    <div class="res-label">White Papers</div>
    <div class="res-title" style="font-size:16px">It is a long established fact that a reader will be distracted</div>
    <a class="btn" href="#">Download</a>
  </div>
</article>
<article class="card abs" style="left:876px;top:3010px;width:236px">
  <div class="photo" style="height:130px" role="img" aria-label="Photo of a keyboard with an FAQ key"></div>
  <div class="inner">
    <div class="res-label">FAQs</div>
    <div class="res-title" style="font-size:16px">It is a long established fact that a reader will be distracted</div>
    <a class="btn" href="#">Read More</a>
  </div>
</article>

<footer class="footer abs"></footer>
<svg class="abs" style="left:0;top:3420px" width="1200" height="90" viewBox="0 0 1200 90" preserveAspectRatio="none" aria-hidden="true">
  <path d="M0 0 L1200 0 L1200 40 C900 90 750 40 600 50 C400 60 250 10 0 50Z" fill="var(--white)"/>
</svg>
<div class="wave-mark abs" style="top:3480px;border-color:var(--light)"></div>

<div class="foot-brand brand abs"><span class="dot"></span>Harborlane<br>Consultants LLC</div>
<div class="foot-contact abs">
  <h4>Dennis Malbrook</h4>
  <div><b>Call Us:</b> 555-201-4830</div>
  <div>E: info@harborlaneconsult.com</div>
  <div><b>Location:</b> Cedar Hollow, VA</div>
  <div style="margin-bottom:10px"><b>Network</b></div>
  <a class="btn" href="#">Exploratory Meeting Now</a>
</div>
<div class="foot-links abs">
  <h4>Quick Links</h4>
  <div>Home</div><div>About</div><div>Services</div><div>Articles</div>
  <div>Videos</div><div>White Papers</div><div>FAQs</div><div>Contact Us</div>
</div>
<div class="map abs" role="img" aria-label="Map of the office location"></div>
<div class="copy abs">© 2022 Harborlane Consultants LLC. All Rights Reserved</div>

</body>
</html>
```